Digital One Pager for Consulting Practice

I would like the essence of the content in my ppt consolidated into a one-pager. The one-pager will mainly be sent via email as a pdf and intended to excite and invite new clients and establish the credibility of my boutique high-end consulting firm. Infographics and symbols would be a plus. The target client should view the firm as providing premeir service. The client is getting a thought partner.

Target Market(s)

Large Medical Device Manufacturer Executives, Early-Stage Medical Device Manufacturer Executives, Partners at VC Firms

Industry/Entity Type

Medical Equipment

Colors
0355a3
f37122

Requirements
Must have
• Please match the color scheme in ppt. Please use the existing logo. I am very open to better graphics on the process. My photo does not need to be on the digital flyer. Hyper link to the website and email is needed.
Nice to have
• Infographics

```html
<!DOCTYPE html>
<html lang="en">
<head>
<meta charset="utf-8">
<title>Halvern Ventures Value</title>
<link rel="stylesheet" href="https://fonts.googleapis.com/css2?family=Crimson+Pro:wght@400;600;700&family=Montserrat:wght@400;600;800&display=swap">
<style>
  :root {
    --navy: #111b2e;
    --orange: #e4503a;
    --red: #9c2a1e;
    --cyan: #27b5dd;
    --ink: #1d1d1f;
    --white: #ffffff;
    --serif: "Crimson Pro", Georgia, serif;
    --sans: "Montserrat", Arial, sans-serif;
  }
  * { box-sizing: border-box; margin: 0; padding: 0; }
  html, body { width: 900px; height: 1200px; overflow: hidden; background: var(--white); }
  .page { position: relative; width: 900px; height: 1200px; overflow: hidden; font-family: var(--serif); color: var(--ink); }
  .backdrop { position: absolute; inset: 0; }
  .abs { position: absolute; }

  .brand { left: 36px; top: 112px; color: var(--white); font-family: var(--sans); font-weight: 600; display: flex; align-items: center; gap: 12px; }
  .brand-dot { width: 18px; height: 18px; border-radius: 50%; background: var(--white); }
  .brand-name { font-size: 30px; line-height: 1; letter-spacing: 3px; }
  .brand-name small { display: block; font-size: 17px; letter-spacing: 5.5px; margin-top: 4px; }

  .title { left: 420px; width: 440px; top: 14px; text-align: center; color: var(--white); font-family: var(--sans); }
  .title-main { font-size: 76px; font-weight: 800; letter-spacing: 2px; line-height: 1; }
  .title-sub { font-size: 41px; font-weight: 400; letter-spacing: 1px; line-height: 1; margin-top: 8px; }

  .content { left: 303px; width: 580px; }
  .heading { color: var(--orange); font-size: 33px; font-weight: 600; line-height: 1; }
  .sub-heading { font-size: 20px; font-weight: 700; line-height: 1.1; color: var(--ink); }
  .body { font-size: 17px; line-height: 1.2; }

  .ticks { list-style: none; margin-top: 10px; }
  .ticks li { position: relative; padding-left: 22px; margin-bottom: 9px; font-size: 17px; line-height: 1.18; }
  .ticks li svg { position: absolute; left: 0; top: 4px; }
  .dots { list-style: none; }
  .dots li { position: relative; padding-left: 19px; font-size: 16.5px; line-height: 1.18; margin-bottom: 9px; }
  .dots li::before { content: ""; position: absolute; left: 2px; top: 7px; width: 8px; height: 8px; border-radius: 50%; background: var(--orange); }
  .dots.sub { margin-left: 33px; margin-top: 4px; }
  .dots.sub li { font-size: 15.5px; margin-bottom: 8px; }

  .services-grid { display: grid; grid-template-columns: 282px 290px; margin-top: 12px; }
  .services-grid .sub-heading { margin-bottom: 7px; }
  .services-grid .dots { margin-bottom: 9px; }

  .provide .sub-heading { font-size: 17px; margin: 10px 0 8px; }
  .provide .dots { margin-left: 22px; }
  .provide .dots li { padding-left: 20px; }

  .partners { display: flex; align-items: center; gap: 16px; margin-top: 16px; }
  .badge { height: 34px; border-radius: 3px; }

  .side-bar-label { left: 0; color: var(--white); font-size: 25px; font-weight: 700; padding-left: 30px; line-height: 32px; }

  .tagline { left: 295px; top: 1062px; width: 605px; height: 34px; display: flex; align-items: center; justify-content: center; color: var(--white); font-size: 19.5px; font-weight: 700; gap: 14px; }
  .tagline .sep { width: 2px; height: 22px; background: var(--orange); }

  .contact { top: 1148px; color: var(--white); font-size: 19px; display: flex; align-items: center; gap: 10px; }
  .contact a { color: var(--white); text-decoration: none; }

  .step-label { font-size: 16px; font-weight: 700; line-height: 1.05; }
  .step-label.left { text-align: right; }
</style>
</head>
<body>
<main class="page">
  <svg class="backdrop" width="900" height="1200" viewBox="0 0 900 1200" aria-hidden="true">
    <polygon points="0,100 327,100 0,432" fill="var(--navy)"/>
    <polygon points="426,0 900,0 900,140 288,140" fill="var(--navy)"/>
    <polygon points="300,140 900,140 900,174 268,174" fill="var(--orange)"/>
    <polygon points="0,100 300,100 244,184 0,184" fill="var(--orange)"/>
    <line x1="812" y1="176" x2="846" y2="138" stroke="var(--white)" stroke-width="5"/>
    <line x1="836" y1="176" x2="870" y2="138" stroke="var(--white)" stroke-width="4"/>
    <!-- side labels -->
    <polygon points="0,456 296,456 276,488 0,488" fill="var(--orange)"/>
    <polygon points="0,762 296,762 276,794 0,794" fill="var(--orange)"/>
    <!-- tagline band -->
    <rect x="295" y="1062" width="605" height="34" fill="var(--navy)"/>
    <!-- footer -->
    <polygon points="380,1108 900,1108 900,1200 318,1200" fill="var(--orange)"/>
    <polygon points="0,1134 376,1134 336,1200 0,1200" fill="var(--navy)"/>
    <line x1="352" y1="1120" x2="394" y2="1064" stroke="var(--navy)" stroke-width="5"/>
    <line x1="376" y1="1120" x2="418" y2="1064" stroke="var(--navy)" stroke-width="3"/>
  </svg>

  <div class="abs brand">
    <span class="brand-dot"></span>
    <span class="brand-name">HALVERN<small>VENTURES</small></span>
  </div>

  <header class="abs title">
    <div class="title-main">HALVERN</div>
    <div class="title-sub">VENTURES VALUE</div>
  </header>

  <section class="abs content" style="top:196px">
    <h2 class="heading">Experience</h2>
    <ul class="ticks">
      <li><svg width="14" height="12" viewBox="0 0 14 12"><path d="M1 6l4 4 8-9" fill="none" stroke="var(--orange)" stroke-width="2.4"/></svg>Over a decade &nbsp;@FDA (Former Deputy Division Director)</li>
      <li><svg width="14" height="12" viewBox="0 0 14 12"><path d="M1 6l4 4 8-9" fill="none" stroke="var(--orange)" stroke-width="2.4"/></svg>Expertise: Cardiovascular, Ophthalmology, General Hospital, Infection Control, Dental, Anesthesia, Respiratory</li>
      <li><svg width="14" height="12" viewBox="0 0 14 12"><path d="M1 6l4 4 8-9" fill="none" stroke="var(--orange)" stroke-width="2.4"/></svg>Vice President Regulatory Affairs / Quality Assurance @Corvant (Fortune 150 Company)</li>
    </ul>
    <ul class="dots sub">
      <li>Initiated reorganization of department</li>
      <li>Led major compliance effort</li>
      <li>Successful FDA inspection (no observations)</li>
    </ul>
  </section>

  <section class="abs content" style="top:455px">
    <h2 class="heading">Services</h2>
    <div class="services-grid">
      <div>
        <h3 class="sub-heading">Regulatory Strategy</h3>
        <ul class="dots"><li>RAQA Organizational Structure</li><li>Regulatory Pathway</li></ul>
        <h3 class="sub-heading">Interim Executive<br>Leadership</h3>
        <ul class="dots"><li>Compliance Remediation</li><li>Accelerated Product Registration</li></ul>
      </div>
      <div>
        <h3 class="sub-heading">FDA Communications</h3>
        <ul class="dots"><li>Deficiency Response</li><li>Application Review</li></ul>
        <h3 class="sub-heading">Training</h3>
        <ul class="dots"><li>FDA Communication</li><li>MDR Reporting</li></ul>
      </div>
    </div>
  </section>

  <section class="abs content provide" style="top:708px">
    <h2 class="heading">Experience to Provide...</h2>
    <h3 class="sub-heading">Executive Application Review</h3>
    <ul class="dots">
      <li>Examples include: Presubmission, IDE, 510(k) , 513(g), PMA, Refuse to &nbsp;Accept, Hold letter</li>
      <li>Troubleshooting</li>
    </ul>
    <h3 class="sub-heading">Strategic Advice &amp; Diligence to Investors</h3>
    <ul class="dots">
      <li>Validate &amp; Verify Founder Milestones</li>
      <li>Diligence portfolio company Regulatory and Quality systems</li>
    </ul>
  </section>

  <section class="abs content" style="top:950px">
    <h2 class="heading" style="font-size:30px">Valued Partner Network</h2>
    <div class="partners" aria-label="Partner network">
      <span class="badge" style="width:62px;background:#3b8fc7"></span>
      <span class="badge" style="width:68px;background:#25356b"></span>
      <span class="badge" style="width:80px;background:var(--navy)"></span>
      <span class="badge" style="width:70px;background:#1f8fd6"></span>
      <span class="badge" style="width:112px;background:#c9c9c9"></span>
      <span class="badge" style="width:80px;background:#2a5fa8"></span>
    </div>
  </section>

  <div class="abs side-bar-label" style="top:456px">Differentiators</div>
  <svg class="abs" style="left:18px;top:506px" width="252" height="222" viewBox="0 0 250 220" role="img" aria-label="Experience, Network and Process combine into Leverage">
    <defs>
      <linearGradient id="gExp" x1="0" y1="1" x2="1" y2="0"><stop offset="0" stop-color="#34c6ee"/><stop offset="1" stop-color="#1a7fb0"/></linearGradient>
      <linearGradient id="gNet" x1="0" y1="0" x2="1" y2="1"><stop offset="0" stop-color="#e0503a"/><stop offset="1" stop-color="#8a1f16"/></linearGradient>
    </defs>
    <polygon points="125,0 0,216 69.5,176 125,80" fill="url(#gExp)"/>
    <polygon points="125,0 250,216 180.5,176 125,80" fill="url(#gNet)"/>
    <polygon points="0,216 250,216 180.5,176 69.5,176" fill="var(--navy)"/>
    <text x="80" y="118" transform="rotate(-60 80 118)" text-anchor="middle" dominant-baseline="middle" fill="#fff" font-family="Crimson Pro, serif" font-size="19" font-weight="600">Experience</text>
    <text x="170" y="118" transform="rotate(60 170 118)" text-anchor="middle" dominant-baseline="middle" fill="#fff" font-family="Crimson Pro, serif" font-size="19" font-weight="600">Network</text>
    <text x="125" y="197" text-anchor="middle" dominant-baseline="middle" fill="#fff" font-family="Crimson Pro, serif" font-size="19" font-weight="700">Process</text>
    <text x="125" y="148" text-anchor="middle" dominant-baseline="middle" fill="var(--navy)" font-family="Crimson Pro, serif" font-size="18" font-weight="700">Leverage</text>
  </svg>

  <div class="abs side-bar-label" style="top:762px">Efficient Process</div>
  <svg class="abs" style="left:110px;top:820px" width="100" height="300" viewBox="0 0 100 300" role="img" aria-label="Four step process">
    <defs>
      <radialGradient id="gBall" cx="0.4" cy="0.35" r="0.7"><stop offset="0" stop-color="#fff"/><stop offset="1" stop-color="#d4d4d4"/></radialGradient>
    </defs>
    <path d="M50 12 A34 34 0 0 0 50 80" fill="none" stroke="var(--orange)" stroke-width="10"/>
    <path d="M50 80 A34 34 0 0 1 50 148" fill="none" stroke="var(--navy)" stroke-width="10"/>
    <path d="M50 148 A34 34 0 0 0 50 216" fill="none" stroke="var(--cyan)" stroke-width="10"/>
    <path d="M50 216 A34 34 0 0 1 50 284" fill="none" stroke="var(--orange)" stroke-width="10"/>
    <g font-family="Montserrat, sans-serif" font-size="20" font-weight="800" text-anchor="middle">
      <circle cx="50" cy="46" r="24" fill="url(#gBall)"/><text x="50" y="53" fill="var(--orange)">1</text>
      <circle cx="50" cy="114" r="24" fill="url(#gBall)"/><text x="50" y="121" fill="var(--navy)">2</text>
      <circle cx="50" cy="182" r="24" fill="url(#gBall)"/><text x="50" y="189" fill="var(--cyan)">3</text>
      <circle cx="50" cy="250" r="24" fill="url(#gBall)"/><text x="50" y="257" fill="var(--orange)">4</text>
    </g>
  </svg>
  <div class="abs step-label" style="left:205px;top:848px;color:var(--orange)">Exploratory<br>Call</div>
  <div class="abs step-label left" style="left:20px;width:84px;top:916px;color:var(--navy)">Regulatory<br>Landscape</div>
  <div class="abs step-label" style="left:205px;top:984px;color:var(--cyan)">Problem<br>Statement</div>
  <div class="abs step-label left" style="left:10px;width:94px;top:1042px;color:var(--orange)">Review &amp;<br>Align on<br>Deliverables</div>

  <div class="abs tagline">
    <span>Extensive Experience</span><span class="sep"></span><span>Efficient Process</span><span class="sep"></span><span>Valued Network</span>
  </div>

  <div class="abs contact" style="left:28px">
    <svg width="20" height="20" viewBox="0 0 24 24"><path d="M6.6 10.8a15.1 15.1 0 0 0 6.6 6.6l2.2-2.2c.3-.3.7-.4 1-.2 1.1.4 2.3.6 3.6.6.6 0 1 .4 1 1V20c0 .6-.4 1-1 1A17 17 0 0 1 3 4c0-.6.4-1 1-1h3.5c.6 0 1 .4 1 1 0 1.3.2 2.5.6 3.6.1.3 0 .7-.2 1z" fill="#fff"/></svg>
    <span>555.014.2290</span>
  </div>
  <div class="abs contact" style="left:398px;font-size:18px">
    <svg width="18" height="14" viewBox="0 0 18 14"><rect x="1" y="1" width="16" height="12" fill="none" stroke="#fff" stroke-width="1.6"/><path d="M1 1l8 7 8-7" fill="none" stroke="#fff" stroke-width="1.6"/></svg>
    <a href="mailto:info@halvernventures.com">info@halvernventures.com</a>
  </div>
  <div class="abs contact" style="left:660px;font-size:18px">
    <svg width="18" height="18" viewBox="0 0 18 18"><circle cx="9" cy="9" r="7.5" fill="none" stroke="#fff" stroke-width="1.5"/><ellipse cx="9" cy="9" rx="3.2" ry="7.5" fill="none" stroke="#fff" stroke-width="1.3"/><path d="M1.5 9h15" stroke="#fff" stroke-width="1.3"/></svg>
    <a href="https://www.halvernventures.com">www.halvernventures.com</a>
  </div>
</main>
</body>
</html>
```